Criação de Papelaria (6 itens) para Automotivo
" Somos uma loja compacta e o nosso diferencial é o bom atendimento personalizado que damos ao cliente, e que a maioria elogia. Compramos, vendemos, trocamos e aceitamos carros consignados. "

```html
<!DOCTYPE html>
<html lang="en">
<head>
<meta charset="UTF-8">
<title>Campo Alto Veículos – Letterhead</title>
<link href="https://fonts.googleapis.com/css2?family=Open+Sans:wght@400;600;700&display=swap" rel="stylesheet">
<style>
  :root{
    --bg:#e9e9e9;
    --paper:#ffffff;
    --orange:#f07c1f;
    --orange-soft:#f6b27a;
    --dark:#3a3a3a;
    --text:#6d6d6d;
    --muted:#9a9a9a;
  }
  *{margin:0;padding:0;box-sizing:border-box}
  html,body{width:1200px;height:1200px;overflow:hidden;background:var(--bg)}
  body{font-family:"Open Sans",Arial,sans-serif;color:var(--text)}
  .letterhead{
    position:absolute;left:220px;top:45px;width:760px;height:1110px;
    background:var(--paper);box-shadow:0 6px 24px rgba(0,0,0,.12);overflow:hidden;
  }
  .top-strip{
    position:absolute;top:0;right:0;width:470px;height:14px;
    background:linear-gradient(90deg,rgba(58,58,58,0),var(--dark) 30%);
  }
  .brand{
    position:absolute;top:80px;right:90px;display:flex;align-items:center;gap:12px;
    font-family:"Open Sans",sans-serif;font-weight:700;font-size:28px;color:var(--dark);
  }
  .brand-mark{width:18px;height:18px;background:var(--orange)}
  .salutation{
    position:absolute;top:165px;left:60px;font-weight:700;font-size:15px;color:var(--orange);
  }
  .body-copy{
    position:absolute;top:198px;left:60px;width:640px;font-size:11.5px;line-height:1.75;color:var(--text);
  }
  .body-copy p{margin-bottom:12px;text-align:justify}
  .sign-off{position:absolute;top:640px;right:80px;width:200px;text-align:center;font-size:11px}
  .sign-off .closing{text-align:left;margin-bottom:8px}
  .signature{display:block;width:150px;height:42px;margin:0 auto 4px;background:linear-gradient(90deg,#f1f1f1,#dcdcdc,#f1f1f1);border-radius:20px}
  .sign-rule{border-top:1px solid #ccc;width:170px;margin:0 auto 4px}
  .sign-name{font-size:11.5px;color:var(--dark)}
  .sign-role{font-size:10px;color:var(--muted)}
  .contacts{
    position:absolute;left:60px;top:850px;width:650px;display:flex;justify-content:space-between;font-size:11.5px;color:var(--text);
  }
  .contact-col{display:flex;flex-direction:column;gap:14px}
  .contact-item{display:flex;align-items:center;gap:10px}
  .icon{width:22px;height:22px;background:var(--orange);border-radius:3px;display:flex;align-items:center;justify-content:center;flex:none}
  .icon svg{width:13px;height:13px}
  .address{line-height:1.4}
  .corner-band{
    position:absolute;left:0;top:840px;width:22px;height:210px;
    background:linear-gradient(180deg,rgba(240,124,31,0),var(--orange));
  }
  .bottom-band{
    position:absolute;left:0;bottom:0;width:100%;height:44px;
    background:linear-gradient(90deg,var(--orange),var(--orange-soft) 60%,rgba(246,178,122,.2));
  }
</style>
</head>
<body>
  <main class="letterhead">
    <div class="top-strip" role="img" aria-label="Checkered racing-flag strip"></div>

    <div class="brand"><span class="brand-mark"></span>Campo Alto Veículos</div>

    <p class="salutation">Dear Mr. Carter</p>

    <section class="body-copy">
      <p>Lorem ipsum dolor sit amet, consectetur adipiscing elit. Vestibulum adipiscing felis ac tellus consectetur feugiat. Etiam commodo sodales eros a rutrum. Sed porta metus eros, mattis sed elit ut, faucibus vel arcu. Sed egestas lorem eros. Nullam consectetur ultricies ipsum. Fusce vel tortor eget ex porta sagittis. Sed volutpat ut volutpat. Vivamus sed pharetra mi, et rhoncus lectus. Donec iaculis gravida mauris. Cras vel dolor vehicula, sodales mi.</p>
      <p>Vivamus eget dui velit. Nulla facilisi. Aliquam erat volutpat. Quisque finibus nisi in magna pellentesque, id rutrum dolor blandit. Nunc quis vulputate erat. Donec pretium tellus eu nisl tristique porttitor. Donec at ante vel lorem posuere molestie. Nulla auctor vel massa et sodales. Suspendisse potenti. Ut non tempor orci. Maecenas sit amet commodo ex, quis luctus nibh. Duis eget odio sed eros lacinia blandit.</p>
      <p>Aenean et congue leo. Aliquam ullamcorper fermentum neque, non egestas nunc vulputate id. Nam ultricies quis nibh at porta. Nullam vel dui eu nisi tempor convallis. Cras non lobortis nisl. Integer sodales ipsum sit amet semper lobortis. Pellentesque volutpat velit quis nunc pretium interdum. Sed eu posuere lectus. Mauris ut orci malesuada, rhoncus nunc at, congue urna. Praesent sagittis at mi et accumsan. Curabitur feugiat purus velit, vel tempor ipsum aliquet non.</p>
      <p>Etiam vel aliquet magna. Duis ornare, mauris vel hendrerit faucibus, felis erat dignissim turpis, quis aliquam sem leo non dolor. Donec et nisl tellus. Proin non metus in neque faucibus feugiat. Phasellus ac tincidunt orci, sed tristique ex. Nam mollis augue sit amet lobortis blandit.</p>
    </section>

    <div class="sign-off">
      <p class="closing">Yours sincerely,</p>
      <span class="signature" role="img" aria-label="Handwritten signature"></span>
      <div class="sign-rule"></div>
      <p class="sign-name">Paul Hart</p>
      <p class="sign-role">Sales Manager</p>
    </div>

    <div class="corner-band" role="img" aria-label="Orange checkered strip"></div>

    <section class="contacts">
      <div class="contact-col">
        <div class="contact-item">
          <span class="icon"><svg viewBox="0 0 24 24"><path fill="#fff" d="M6.6 10.8c1.4 2.8 3.8 5.1 6.6 6.6l2.2-2.2c.3-.3.7-.4 1-.2 1.1.4 2.3.6 3.6.6.6 0 1 .4 1 1V20c0 .6-.4 1-1 1C10.6 21 3 13.4 3 4c0-.6.4-1 1-1h3.5c.6 0 1 .4 1 1 0 1.3.2 2.5.6 3.6.1.3 0 .7-.2 1z"/></svg></span>
          (62) 3417-2290
        </div>
        <div class="contact-item">
          <span class="icon"><svg viewBox="0 0 24 24"><path fill="#fff" d="M12 3C7 3 3 6.6 3 11c0 2 .8 3.8 2.2 5.2L4 21l4.4-1.8c1.1.4 2.3.6 3.6.6 5 0 9-3.6 9-8s-4-8.8-9-8.8z"/></svg></span>
          (62) 9 8143-7725
        </div>
      </div>
      <div class="contact-col">
        <div class="contact-item">
          <span class="icon"><svg viewBox="0 0 24 24"><path fill="#fff" d="M3 5h18v14H3z"/><path fill="none" stroke="#f07c1f" stroke-width="2" d="M3 6l9 7 9-7"/></svg></span>
          contato@campoaltoveiculos.com.br
        </div>
        <div class="contact-item">
          <span class="icon"><svg viewBox="0 0 24 24"><circle cx="12" cy="12" r="8.5" fill="none" stroke="#fff" stroke-width="2"/><path fill="none" stroke="#fff" stroke-width="1.6" d="M3.5 12h17M12 3.5c3 3 3 14 0 17M12 3.5c-3 3-3 14 0 17"/></svg></span>
          www.campoaltoveiculos.com.br
        </div>
      </div>
      <div class="contact-col">
        <div class="contact-item">
          <span class="icon"></span>
          Campo Alto Veículos
        </div>
        <div class="contact-item">
          <span class="icon"><svg viewBox="0 0 24 24"><path fill="#fff" d="M12 2a7 7 0 0 0-7 7c0 5 7 13 7 13s7-8 7-13a7 7 0 0 0-7-7zm0 9.5A2.5 2.5 0 1 1 12 6.5a2.5 2.5 0 0 1 0 5z"/></svg></span>
          <span class="address">Rua dos Ipês, 1180 - Setor Bela Vista,<br>Goiânia - GO</span>
        </div>
      </div>
    </section>

    <div class="bottom-band" role="img" aria-label="Orange checkered racing-flag band"></div>
  </main>
</body>
</html>
```